Dr Mira Thalen, Orthopaedic Hand Surgeon

I am an orthopaedic hand surgeon and need business cards that reflect the surgery I do. I operate on bones, ligaments, tendons, and soft tissues. I can do microsurgery (surgery under an operating microscope) - including connecting ends of cut nerves and arteries in the fingers together. As an orthopaedic surgeon, I also fix fractures and manage orthopaedic trauma in the rest of the body. I favour black as a colour, and have some pictures of hand X-rays that you can use in the design, if you think that would look good (feel free to crop).
Updates

Hi all. Thank you for all your submissions so far. Please note that I have updated my project brief. I would like to emphasise that use of the logos that I have provided is optional, and if used, I would very much prefer the logo not to dominate the card, but add to the overall aesthetic of the card. Warm regards, Mira

Target Market(s)

Referring medical practitioners, hand therapists, patients

Industry/Entity Type

Healthcare

Contact Information for Business Card

Dr Mira Thalen
Orthopaedic Hand Surgeon
MBBS BSc (Med), MIntPH (Merit), FCWES (Ortho), FUPelV

Font styles to use
Serif

Colors

Designer to choose colors to be used in the design.

Requirements
Must have
• Space for:
• 2 addresses (a PO Box Address and a consulting suite address) - to be confirmed
• 1 phone number - to be confirmed
Nice to have
• Please choose one of the FCWES logos (I included 3 - colour, black reverse, and greyscale); if you include this in the design, IT SHOULD NOT DOMINATE THE CARD, but be smaller and more discreet.
• I have also attached the FUPelV logo (colour and greyscale); if you choose to include this in the design, IT SHOULD NOT DOMINATE THE CARD, but be smaller and more discreet.
• I would love to be able to update details on the card as time goes on, and thus would like to own the template for the card as well.
• Also I would love discussion with regard to any changes on the card, if I am not completely happy with the design, and would like to discuss things such as ease of printing, finish on the cards (matte, polish) etc.
Should not have
• I don't like the card to look too crowded

```html
<!DOCTYPE html>
<html lang="en">
<head>
<meta charset="utf-8">
<title>Dr Mira Thalen – Business Card</title>
<link href="https://fonts.googleapis.com/css2?family=Cinzel:wght@500;600&family=PT+Sans:wght@400;700&display=swap" rel="stylesheet">
<style>
  :root {
    --stage: #1c1c1c;
    --card-white: #ffffff;
    --ink: #1d1d1d;
    --brand-blue: #1c5d85;
    --brand-navy: #1e4a6e;
    --muted-grey: #6a6a6a;
    --rule-red: #e0585c;
    --back-top: #04476a;
    --back-bottom: #0a5476;
    --crest-fill: #e9ecef;
  }
  * { margin: 0; padding: 0; box-sizing: border-box; }
  html, body { width: 1200px; height: 900px; overflow: hidden; background: var(--stage); }
  .stage { position: relative; width: 1200px; height: 900px; }

  .card {
    position: absolute; top: 170px; width: 347px; height: 561px;
    box-shadow: 3px 4px 8px rgba(0,0,0,.55);
  }
  .card-front { left: 259px; background: var(--card-white); }
  .card-back {
    left: 631px;
    background: linear-gradient(180deg, var(--back-top) 0%, var(--back-bottom) 100%);
    overflow: hidden;
  }

  .fellow-mark { position: absolute; left: 42px; top: 98px; display: flex; align-items: center; gap: 10px; }
  .fellow-square { width: 16px; height: 16px; background: var(--brand-navy); }
  .fellow-name {
    font-family: "Cinzel", serif; font-weight: 500; font-size: 34px;
    color: var(--brand-navy); letter-spacing: 0.5px; line-height: 1;
  }
  .fellow-caption {
    position: absolute; right: 42px; top: 134px; text-align: right;
    font-family: "PT Sans", sans-serif; font-size: 11px; line-height: 15px; color: var(--muted-grey);
  }

  .details { position: absolute; left: 0; top: 266px; width: 100%; text-align: center; font-family: "PT Sans", sans-serif; color: var(--ink); }
  .doctor-name {
    font-family: "Cinzel", serif; font-weight: 600; font-size: 22px;
    color: var(--brand-blue); letter-spacing: 1px; line-height: 28px;
  }
  .specialty { font-size: 15px; line-height: 20px; margin-top: 0; }
  .credentials { font-size: 14.5px; line-height: 21px; margin-top: 6px; }
  .rule { width: 193px; height: 1.5px; background: var(--rule-red); margin: 11px auto 0; }
  .contact { font-size: 15px; line-height: 21px; margin-top: 11px; }
  .contact .label { font-weight: 700; color: var(--brand-blue); }
  .address { font-size: 15px; line-height: 20px; margin-top: 8px; }
  .address + .address { margin-top: 6px; }

  .back-glow {
    position: absolute; left: -60px; top: 390px; width: 467px; height: 330px; border-radius: 50%;
    background: radial-gradient(ellipse at center top, rgba(255,255,255,.06), rgba(255,255,255,0) 70%);
  }
  .crest-area {
    position: absolute; left: 86px; top: 157px; width: 176px; height: 248px;
    border-radius: 14px 14px 40px 40px;
    background: linear-gradient(180deg, #f4f6f8 0%, var(--crest-fill) 100%);
  }
</style>
</head>
<body>
<main class="stage">
  <section class="card card-front" aria-label="Card front">
    <div class="fellow-mark">
      <span class="fellow-square"></span>
      <span class="fellow-name">FCWES</span>
    </div>
    <p class="fellow-caption">Fellow of the<br>Coastal Western Extremity Surgeons</p>

    <div class="details">
      <h1 class="doctor-name">DR&nbsp; MIRA THALEN</h1>
      <p class="specialty">Orthopaedic Hand Surgeon</p>
      <p class="credentials">MBBS BSc (Med), MIntPH (Merit),<br>FCWES (Ortho), FUPelV</p>
      <div class="rule"></div>
      <p class="contact"><span class="label">P:</span> (044)123456789<br><span class="label">E:</span> info@youremail.com</p>
      <div class="rule"></div>
      <p class="address">1234, Address1 GoesHere,<br>Country name, 12345</p>
      <p class="address">1234, Address2 GoesHere,<br>Country name, 12345</p>
    </div>
  </section>

  <section class="card card-back" aria-label="Card back">
    <div class="back-glow"></div>
    <div class="crest-area" role="img" aria-label="Society crest emblem in black and white"></div>
  </section>
</main>
</body>
</html>
```